Vet Project for Web Application

We are developing a web app / forms to allow a Vet to record information when visiting a farm - eg to test animals for TB.
Needs to be clean and fresh, not cluttered.
Using standard web form design elements so that the user don't have to think.
Needs to use elements of the colours from the logo.

We will need a standard template page which we can base each of our webforms on, so we will need
standard web elements (labels, text boxes, radio buttons etc)
data grids
buttons
menus
error messages

Target Market(s)

Vets for farm animals

Number of Pages Required

1 page

Font styles to use
Sans Serif

Requirements
Must have
• Simple form elements. Intuitive. Obvious. Follow the colour pallette in the logo
Should not have
• elements that need instruction to use

```html
<!DOCTYPE html>
<html lang="en">
<head>
<meta charset="utf-8">
<title>HerdCheck – Add Record</title>
<link href="https://fonts.googleapis.com/css2?family=Mulish:wght@400;500;600;700;800&family=Montserrat:wght@700;800&display=swap" rel="stylesheet">
<style>
:root{
  --brand-blue:#4a9fd1;
  --brand-green:#b5cc5a;
  --ink:#222;
  --muted:#555;
  --line:#6b6b6b;
  --sidebar-bg:#f5f5f5;
  --divider:#dcdcdc;
  --header-grey:#8e8f93;
  --row-alt:#f4f4f4;
  --edit:#8cc152;
  --delete:#e4331a;
}
*{box-sizing:border-box;margin:0;padding:0}
html,body{width:1200px;height:666px;overflow:hidden;background:#fff;font-family:"Mulish",sans-serif;color:var(--ink)}
.app{position:relative;width:1200px;height:666px}
.sidebar{position:absolute;left:0;top:0;width:193px;height:666px;background:var(--sidebar-bg)}
.brand{position:absolute;left:30px;top:24px;display:flex;align-items:center;gap:8px;font-size:27px;font-weight:500;color:var(--brand-blue);letter-spacing:1px}
.brand-dot{width:12px;height:12px;background:var(--brand-green);border-radius:50%}
.nav{position:absolute;left:22px;top:116px;width:156px;list-style:none}
.nav li{height:49.5px;display:flex;align-items:center;gap:8px;padding-left:12px;font-size:14px;border-bottom:1px solid var(--divider)}
.nav li:last-child{border-bottom:none}
.nav li.active{color:var(--brand-blue)}
.nav svg{width:12px;height:12px;flex:none}
.topbar{position:absolute;left:193px;top:0;right:0;height:61px;background:#fff;box-shadow:0 2px 4px rgba(0,0,0,.05)}
.burger{position:absolute;left:30px;top:24px}
.tools{position:absolute;right:20px;top:14px;display:flex;align-items:center;gap:14px}
.bell{position:relative}
.badge{position:absolute;right:-4px;top:-4px;width:12px;height:12px;border-radius:50%;background:var(--brand-green);color:#fff;font-size:9px;text-align:center;line-height:12px}
.avatar{width:30px;height:30px;border-radius:50%;background:linear-gradient(#cfe3ee,#7aa7c2)}
.user{font-size:14px;font-weight:500;display:flex;align-items:center;gap:10px}
.page-title{position:absolute;left:225px;top:98px;font-family:"Montserrat",sans-serif;font-weight:800;font-size:16px}
.field{position:absolute;width:305px;height:42px;border:1px solid var(--line);padding-left:14px;display:flex;align-items:center;font-size:11.5px;color:#333}
.select::after{content:"";position:absolute;right:12px;top:18px;border:4px solid transparent;border-top:5px solid #222}
.gender{position:absolute;left:874px;top:128px;font-size:11.5px;color:#333}
.radios{display:flex;gap:22px;margin-top:10px}
.radio{display:flex;align-items:center;gap:8px}
.radio i{width:13px;height:13px;border-radius:50%;background:#8a8a8a}
.submit{position:absolute;left:871px;top:244px;width:306px;height:42px;background:var(--brand-green);color:#fff;border:none;font-family:"Montserrat",sans-serif;font-weight:800;font-size:17px;letter-spacing:.5px}
.grid{position:absolute;left:225px;top:316px;width:952px;border-collapse:collapse;font-size:12px;box-shadow:0 1px 4px rgba(0,0,0,.15)}
.grid th{background:var(--header-grey);color:#fff;font-weight:600;height:30px;border-right:1px solid #bbb}
.grid td{height:40px;border-right:1px solid #ddd;text-align:center}
.grid th:last-child,.grid td:last-child{border-right:none}
.grid td.left{text-align:left;padding-left:24px}
.grid td.loc,.grid td.reason{text-align:left;padding-left:18px}
.grid tbody tr:nth-child(even) td{background:var(--row-alt)}
.actions{display:flex;justify-content:center;align-items:center;gap:8px}
.actions .sep{width:1px;height:16px;background:#ddd}
.footer{position:absolute;left:193px;right:0;top:620px;text-align:center;font-size:12px}
</style>
</head>
<body>
<div class="app">
  <aside class="sidebar">
    <div class="brand"><span>HerdCheck</span><span class="brand-dot"></span></div>
    <ul class="nav">
      <li class="active"><svg viewBox="0 0 12 12" fill="none" stroke="currentColor"><path d="M1 6 6 1.5 11 6M2.5 5v6h7V5"/></svg>Dashboard</li>
      <li><svg viewBox="0 0 12 12" fill="none" stroke="currentColor"><path d="M2.5 1h5l2 2v8h-7zM4 6h4M4 8h4"/></svg>Records</li>
      <li><svg viewBox="0 0 12 12" fill="none" stroke="currentColor"><circle cx="6" cy="6" r="4.5"/><path d="M6 5v3.5M6 3.5v.5"/></svg>Information</li>
      <li><svg viewBox="0 0 12 12" fill="none" stroke="currentColor"><path d="M6 10.5 1.5 6A2.5 2.5 0 0 1 6 3a2.5 2.5 0 0 1 4.5 3z"/><path d="M2.5 6h2l1-1.5 1 3 1-1.5h2"/></svg>Health</li>
      <li><svg viewBox="0 0 12 12" fill="none" stroke="currentColor"><path d="M1.5 2h9v6.5h-6l-2 2v-2h-1z"/><path d="M3.5 4.5h5M3.5 6.5h3"/></svg>Messages</li>
      <li><svg viewBox="0 0 12 12" fill="none" stroke="currentColor"><circle cx="6" cy="6" r="1.8"/><circle cx="6" cy="6" r="4.3" stroke-dasharray="2 1.2"/></svg>Settings</li>
    </ul>
  </aside>

  <header class="topbar">
    <svg class="burger" width="20" height="16" viewBox="0 0 20 16"><rect width="20" height="3" fill="#555"/><rect y="6.5" width="20" height="3" fill="#555"/><rect y="13" width="20" height="3" fill="#555"/></svg>
    <div class="tools">
      <svg width="22" height="22" viewBox="0 0 22 22" fill="none" stroke="#999" stroke-width="2.4"><circle cx="9" cy="9" r="6.5"/><path d="M14 14l6 6"/></svg>
      <span class="bell"><svg width="24" height="24" viewBox="0 0 24 24" fill="none" stroke="#999" stroke-width="1.5"><path d="M5 18h14l-2-3v-5a5 5 0 0 0-10 0v5zM10 20a2 2 0 0 0 4 0"/></svg><span class="badge">0</span></span>
      <div class="avatar" role="img" aria-label="User profile photo"></div>
      <span class="user">Alan Porter<svg width="9" height="6" viewBox="0 0 9 6"><path d="M0 0h9L4.5 6z" fill="#222"/></svg></span>
    </div>
  </header>

  <h1 class="page-title">ADD RECORD</h1>

  <div class="field" style="left:226px;top:130px">Vet Name</div>
  <div class="field" style="left:549px;top:130px">Vet Age</div>
  <div class="gender">Gender
    <div class="radios"><span class="radio"><i></i>Male</span><span class="radio"><i></i>Female</span></div>
  </div>
  <div class="field" style="left:226px;top:187px">Weight</div>
  <div class="field" style="left:549px;top:187px">Color</div>
  <div class="field select" style="left:871px;top:187px;width:306px">Number of Animales</div>
  <div class="field" style="left:226px;top:244px">Farm location</div>
  <div class="field" style="left:549px;top:244px">Reason</div>
  <button class="submit">SUBMIT</button>

  <table class="grid">
    <colgroup><col style="width:204px"><col style="width:71px"><col style="width:68px"><col style="width:63px"><col style="width:62px"><col style="width:93px"><col style="width:112px"><col style="width:214px"><col style="width:65px"></colgroup>
    <thead><tr><th>Vet Name</th><th>Vet Age</th><th>Gender</th><th>Weight</th><th>Color</th><th>No.of animals</th><th>Location</th><th>Reason</th><th>Action</th></tr></thead>
    <tbody>
      <tr><td class="left">Cookie</td><td>8</td><td>Male</td><td>20</td><td>Brown</td><td>1</td><td class="loc">Allentown</td><td class="reason">Lorem Ipsum is simply dummy</td><td><div class="actions"><svg width="13" height="13" viewBox="0 0 13 13" fill="none" stroke="#8cc152" stroke-width="1.2"><path d="M9 2H1.5v9.5H11V6"/><path d="M5 8l.5-2L11 .8l1.2 1.2L6.9 7.5z"/></svg><span class="sep"></span><svg width="11" height="13" viewBox="0 0 11 13" fill="#e4331a"><rect y="1.5" width="11" height="1.5"/><rect x="4" width="3" height="1.5"/><path d="M1.5 4h8l-.7 9H2.2z"/></svg></div></td></tr>
      <tr><td class="left">Lydia</td><td>12</td><td>Female</td><td>15</td><td>White</td><td>3</td><td class="loc">Orlando</td><td class="reason">Contrary to popular belief</td><td><div class="actions"><svg width="13" height="13" viewBox="0 0 13 13" fill="none" stroke="#8cc152" stroke-width="1.2"><path d="M9 2H1.5v9.5H11V6"/><path d="M5 8l.5-2L11 .8l1.2 1.2L6.9 7.5z"/></svg><span class="sep"></span><svg width="11" height="13" viewBox="0 0 11 13" fill="#e4331a"><rect y="1.5" width="11" height="1.5"/><rect x="4" width="3" height="1.5"/><path d="M1.5 4h8l-.7 9H2.2z"/></svg></div></td></tr>
      <tr><td class="left">Cowles</td><td>5</td><td>Male</td><td>31</td><td>Black</td><td>2</td><td class="loc">Miami</td><td class="reason">There are many variations of</td><td><div class="actions"><svg width="13" height="13" viewBox="0 0 13 13" fill="none" stroke="#8cc152" stroke-width="1.2"><path d="M9 2H1.5v9.5H11V6"/><path d="M5 8l.5-2L11 .8l1.2 1.2L6.9 7.5z"/></svg><span class="sep"></span><svg width="11" height="13" viewBox="0 0 11 13" fill="#e4331a"><rect y="1.5" width="11" height="1.5"/><rect x="4" width="3" height="1.5"/><path d="M1.5 4h8l-.7 9H2.2z"/></svg></div></td></tr>
      <tr><td class="left">Owens</td><td>3</td><td>Female</td><td>25</td><td>White</td><td>6</td><td class="loc">Fresno</td><td class="reason">It is a long established fact</td><td><div class="actions"><svg width="13" height="13" viewBox="0 0 13 13" fill="none" stroke="#8cc152" stroke-width="1.2"><path d="M9 2H1.5v9.5H11V6"/><path d="M5 8l.5-2L11 .8l1.2 1.2L6.9 7.5z"/></svg><span class="sep"></span><svg width="11" height="13" viewBox="0 0 11 13" fill="#e4331a"><rect y="1.5" width="11" height="1.5"/><rect x="4" width="3" height="1.5"/><path d="M1.5 4h8l-.7 9H2.2z"/></svg></div></td></tr>
      <tr><td class="left">Beverly</td><td>1</td><td>Male</td><td>10</td><td>Brown</td><td>5</td><td class="loc">Mer Rouge</td><td class="reason">Lorem Ipsum is simply dummy</td><td><div class="actions"><svg width="13" height="13" viewBox="0 0 13 13" fill="none" stroke="#8cc152" stroke-width="1.2"><path d="M9 2H1.5v9.5H11V6"/><path d="M5 8l.5-2L11 .8l1.2 1.2L6.9 7.5z"/></svg><span class="sep"></span><svg width="11" height="13" viewBox="0 0 11 13" fill="#e4331a"><rect y="1.5" width="11" height="1.5"/><rect x="4" width="3" height="1.5"/><path d="M1.5 4h8l-.7 9H2.2z"/></svg></div></td></tr>
      <tr><td class="left">Plumley</td><td>20</td><td>Female</td><td>30</td><td>Black</td><td>3</td><td class="loc">Sophia</td><td class="reason">Contrary to popular belief</td><td><div class="actions"><svg width="13" height="13" viewBox="0 0 13 13" fill="none" stroke="#8cc152" stroke-width="1.2"><path d="M9 2H1.5v9.5H11V6"/><path d="M5 8l.5-2L11 .8l1.2 1.2L6.9 7.5z"/></svg><span class="sep"></span><svg width="11" height="13" viewBox="0 0 11 13" fill="#e4331a"><rect y="1.5" width="11" height="1.5"/><rect x="4" width="3" height="1.5"/><path d="M1.5 4h8l-.7 9H2.2z"/></svg></div></td></tr>
    </tbody>
  </table>

  <footer class="footer">Copyright © 2022 All Rights Reserved</footer>
</div>
</body>
</html>
```